BRD business cards Dr. Martin Velk

I need a business card designed for our dental office. We are a "general dental" practice.
Looking for a clean, professional but not too fancy design with our logo and contact information required.
front of card is information/standard business card, backside is appt reminder with lines for date and time of appt
doctors name: Dr. Martin Velk DMD
office name: Velk Family Dental
address: 4827 E Tolland Ave Coral Springs, FL 33065
phone: 954-555-0173
Dentistry
Office name, Doctor name, address, phone number...etc
- White/off white base color, blue and or black lettering

```html
<!DOCTYPE html>
<html lang="en">
<head>
<meta charset="utf-8">
<title>Velk Family Dental – Business Card &amp; Appointment Card</title>
<link href="https://fonts.googleapis.com/css2?family=EB+Garamond:wght@400;600;700&family=Oswald:wght@600&display=swap" rel="stylesheet">
<style>
  :root {
    --ink: #0d0d0d;
    --paper: #ffffff;
    --backdrop: #d9d9d8;
    --rule: #1a1a1a;
  }
  * { box-sizing: border-box; margin: 0; padding: 0; }
  html, body {
    width: 1200px; height: 801px; overflow: hidden;
    background: var(--backdrop);
  }
  .stage { position: relative; width: 1200px; height: 801px; }

  .card {
    position: absolute;
    background: var(--paper);
    box-shadow: 0 6px 18px rgba(0,0,0,.18);
    overflow: hidden;
  }

  /* Practice name: plain text, one colour, one weight */
  .practice-name {
    font-family: "EB Garamond", serif; font-weight: 600;
    font-size: 30px; line-height: 1.1; text-align: center;
  }

  /* ---------- Front: business card ---------- */
  .card-front { left: 110px; top: 90px; width: 350px; height: 600px; }
  .front-band {
    position: absolute; left: 0; right: 0; bottom: 0; height: 330px;
    background: var(--ink);
  }
  .front-step {
    position: absolute; left: 0; top: 230px; width: 175px; height: 60px;
    background: var(--ink);
  }
  .card-front .practice-name {
    position: absolute; top: 60px; left: 20px; right: 20px; color: var(--ink);
  }

  .doctor-name {
    position: absolute; left: 30px; right: 20px; top: 420px;
    font-family: "Oswald", sans-serif; font-weight: 600; font-size: 27px;
    line-height: 1.2; color: var(--paper); letter-spacing: .5px; text-transform: uppercase;
  }
  .contact {
    position: absolute; left: 30px; right: 20px; top: 476px; list-style: none;
    font-family: "EB Garamond", serif; font-size: 17px; line-height: 1.3;
    color: var(--paper);
  }
  .contact li { display: flex; gap: 6px; align-items: flex-start; }
  .contact svg { width: 11px; height: 11px; margin-top: 5px; flex: none; fill: var(--paper); }

  /* ---------- Back: appointment card ---------- */
  .card-back { left: 520px; top: 250px; width: 600px; height: 345px; }
  .back-band {
    position: absolute; left: 0; right: 0; top: 0; height: 92px;
    background: var(--ink);
  }
  .card-back .practice-name {
    position: absolute; top: 28px; left: 0; right: 0; color: var(--paper);
  }

  .appointment {
    position: absolute; left: 36px; right: 36px; top: 112px;
    font-family: "EB Garamond", serif; color: var(--ink);
  }
  .appointment h2 {
    font-weight: 700; font-size: 24px; text-align: center; letter-spacing: .5px;
    margin-bottom: 10px;
  }
  .field-row { display: flex; align-items: baseline; gap: 8px; font-size: 19px; margin-top: 12px; }
  .field-row .blank { flex: 1; border-bottom: 2px dashed var(--rule); height: 1px; }
  .field-row .unit { font-size: 16px; }
  .days { display: flex; justify-content: center; gap: 26px; font-size: 19px; margin-top: 18px; }
  .days label { display: flex; align-items: center; gap: 8px; }
  .days .box { width: 18px; height: 18px; border: 1.8px solid var(--ink); display: inline-block; }
</style>
</head>
<body>
<main class="stage">

  <section class="card card-front" aria-label="Business card front">
    <div class="front-band"></div>
    <div class="front-step"></div>
    <div class="practice-name">Velk Family Dental</div>
    <h1 class="doctor-name">Dr. Martin Velk DMD</h1>
    <ul class="contact">
      <li>
        <svg viewBox="0 0 24 24" aria-hidden="true"><path d="M6.6 10.8a15.1 15.1 0 0 0 6.6 6.6l2.2-2.2a1 1 0 0 1 1-.25 11.4 11.4 0 0 0 3.6.57 1 1 0 0 1 1 1V20a1 1 0 0 1-1 1A17 17 0 0 1 3 4a1 1 0 0 1 1-1h3.5a1 1 0 0 1 1 1c0 1.25.2 2.45.57 3.57a1 1 0 0 1-.25 1z"/></svg>
        <span>954-555-0173</span>
      </li>
      <li>
        <svg viewBox="0 0 24 24" aria-hidden="true"><path d="M12 2a7 7 0 0 0-7 7c0 5.25 7 13 7 13s7-7.75 7-13a7 7 0 0 0-7-7zm0 9.5A2.5 2.5 0 1 1 12 6.5a2.5 2.5 0 0 1 0 5z"/></svg>
        <span>4827 E Tolland Ave Palm Hollow,<br>FL 33981</span>
      </li>
    </ul>
  </section>

  <section class="card card-back" aria-label="Appointment reminder card">
    <div class="back-band"></div>
    <div class="practice-name">Velk Family Dental</div>
    <div class="appointment">
      <h2>YOUR NEXT APPOINTMENT</h2>
      <div class="field-row"><span>Patient name:</span><span class="blank"></span></div>
      <div class="field-row"><span>Day:</span><span class="blank"></span><span>Date:</span><span class="blank"></span><span>Time</span><span class="blank"></span><span class="unit">AM/PM</span></div>
      <div class="field-row"><span>Day:</span><span class="blank"></span><span>Date:</span><span class="blank"></span><span>Time</span><span class="blank"></span><span class="unit">AM/PM</span></div>
      <div class="days">
        <label><span class="box"></span>Mon</label>
        <label><span class="box"></span>Tue</label>
        <label><span class="box"></span>Wed</label>
        <label><span class="box"></span>Thu</label>
        <label><span class="box"></span>Fri</label>
      </div>
    </div>
  </section>

</main>
</body>
</html>
```